Supplement Company Needs a Protein Powder Pouch Design

We are looking for a modern and fresh design for our 500g pouches of protein powder as our current design is not eye catching or exciting enough.

This new design will be printed on both sides of a 178mm x 280mm x 101mm pouch.

We have 4 flavours. These are Banana Ice Cream, Chocolate Deluxe, Strawberries & Cream and Vanilla Ice Cream.

Industry/Entity Type

Supplement

Requirements
Must have
• Attractive and eye catching front and space for all the nutritional information and ingredients on the back.

Must clearly state 'food supplement' somewhere on the front of the pouch.
Nice to have
• Our logo is attached.
Should not have
• No health claims as these are not allowed in the UK

```html
<!DOCTYPE html>
<html lang="en">
<head>
<meta charset="utf-8">
<title>Verve Supplements – Protein Powder Pouches</title>
<link href="https://fonts.googleapis.com/css2?family=Montserrat:wght@200;300;400;500;600;700;800;900&display=swap" rel="stylesheet">
<style>
  :root{
    --stage:#e4e4e4;
    --pouch-black:#111111;
    --berry-red:#d4123a;
    --berry-deep:#a80d2c;
    --cream:#f1efea;
    --band-pink:#e58aa0;
    --brand-blue:#1f8fcf;
    --leaf-green:#8cc63f;
    --banana-yellow:#f3d21b;
    --white:#ffffff;
    --ink:#2a2a2a;
  }
  *{margin:0;padding:0;box-sizing:border-box}
  html,body{width:1200px;height:907px;overflow:hidden}
  body{background:var(--stage);font-family:"Montserrat",sans-serif;position:relative}

  .pouch{position:absolute;top:160px;width:390px;height:615px;border-radius:14px;overflow:hidden;background:var(--pouch-black)}
  .pouch--strawberry{left:110px}
  .pouch--banana{left:675px}

  .brand{position:absolute;display:flex;align-items:center;gap:10px;font-weight:700}
  .brand__dot{width:14px;height:14px;border-radius:50%;background:var(--leaf-green);flex:none}
  .brand__name{display:flex;flex-direction:column;line-height:1}
  .brand__word{font-size:46px;letter-spacing:-1px}
  .brand__sub{font-size:10px;letter-spacing:5.5px;margin-top:4px}
  .pouch--strawberry .brand{left:92px;top:118px;color:var(--brand-blue)}
  .pouch--banana .brand{left:186px;top:150px;color:var(--white)}
  .pouch--banana .brand__word{font-size:44px}

  .strawberry__art{position:absolute;inset:0}
  .strawberry__title{position:absolute;left:0;right:0;top:272px;text-align:center;color:var(--cream)}
  .strawberry__protein{font-size:54px;font-weight:800;letter-spacing:1px;line-height:1}
  .strawberry__powder{font-size:24px;font-weight:300;letter-spacing:12px;margin-top:4px;padding-left:12px}
  .flavour-band{position:absolute;left:60px;right:0;top:474px;height:28px;background:linear-gradient(90deg,rgba(229,138,160,0),var(--band-pink) 30%);color:var(--berry-deep);font-size:14px;font-weight:500;text-align:right;padding:6px 12px 0 0}
  .strawberry__rule{position:absolute;left:20px;right:20px;top:560px;border-top:1px dashed #8a8a8a}
  .pack-info{position:absolute;text-align:center;color:#555}
  .strawberry__info{left:0;right:0;top:562px}
  .pack-info__weight{font-size:14px;font-weight:500}
  .pack-info__label{font-size:10px;letter-spacing:1.5px;font-weight:500}

  .banana__strip{position:absolute;left:15px;top:230px;width:46px;bottom:0;background:var(--banana-yellow);border-top-right-radius:22px}
  .vertical{position:absolute;transform-origin:left top;transform:rotate(-90deg);white-space:nowrap}
  .banana__protein{left:78px;top:592px;font-size:50px;font-weight:200;letter-spacing:14px;color:#e8e8e8}
  .banana__powder{left:138px;top:592px;font-size:34px;font-weight:300;letter-spacing:25px;color:var(--leaf-green)}
  .banana__flavour{position:absolute;left:192px;top:272px;color:var(--white);font-weight:400;line-height:1.15}
  .banana__flavour-main{font-size:38px}
  .banana__flavour-sub{font-size:30px;font-weight:300}
  .banana__panel{position:absolute;left:175px;top:395px;right:0;bottom:0;background:var(--banana-yellow);border-top-left-radius:24px}
  .banana__photo{position:absolute;left:10px;right:10px;top:-20px;height:110px;border-radius:8px;background:radial-gradient(ellipse at 50% 50%,#e9b31e 0%,#f0c52a 45%,rgba(243,210,27,0) 75%)}
  .banana__info{left:0;right:0;top:128px;color:var(--ink)}
  .banana__info .pack-info__weight{font-size:20px;font-weight:700}
  .banana__info .pack-info__label{font-size:11px;font-weight:600;margin-top:6px}
</style>
</head>
<body>

<section class="pouch pouch--strawberry">
  <svg class="strawberry__art" width="390" height="615" viewBox="0 0 390 615">
    <path d="M0 262 Q195 246 390 256 L390 372 Q195 392 0 424 Z" fill="var(--berry-red)"/>
  </svg>
  <svg class="strawberry__art" width="390" height="615" viewBox="0 0 390 615" role="img" aria-label="Photo of two strawberries on whipped cream">
    <defs>
      <radialGradient id="berryGlow" cx="0.3" cy="0.2" r="0.5">
        <stop offset="0" stop-color="#c3202c"/>
        <stop offset="0.5" stop-color="#e7a3a3"/>
        <stop offset="1" stop-color="var(--cream)"/>
      </radialGradient>
    </defs>
    <path d="M0 424 Q195 392 390 372 L390 615 L0 615 Z" fill="url(#berryGlow)"/>
  </svg>

  <div class="brand">
    <span class="brand__dot"></span>
    <span class="brand__name"><span class="brand__word">VERVE</span><span class="brand__sub">SUPPLEMENTS</span></span>
  </div>

  <div class="strawberry__title">
    <div class="strawberry__protein">PROTEIN</div>
    <div class="strawberry__powder">POWDER</div>
  </div>

  <div class="flavour-band">Strawberry &amp; Cream</div>
  <div class="strawberry__rule"></div>
  <div class="pack-info strawberry__info">
    <div class="pack-info__weight">500g</div>
    <div class="pack-info__label">FOOD SUPPLEMENT</div>
  </div>
</section>

<section class="pouch pouch--banana">
  <div class="banana__strip"></div>
  <div class="vertical banana__protein">PROTEIN</div>
  <div class="vertical banana__powder">POWDER</div>

  <div class="brand">
    <span class="brand__dot"></span>
    <span class="brand__name"><span class="brand__word">VERVE</span><span class="brand__sub">SUPPLEMENTS</span></span>
  </div>

  <div class="banana__flavour">
    <div class="banana__flavour-main">Banana</div>
    <div class="banana__flavour-sub">Ice Cream</div>
  </div>

  <div class="banana__panel">
    <div class="banana__photo" role="img" aria-label="Photo of a bunch of ripe bananas"></div>
    <div class="pack-info banana__info">
      <div class="pack-info__weight">500g</div>
      <div class="pack-info__label">FOOD SUPPLEMENT</div>
    </div>
  </div>
</section>

</body>
</html>
```